Varnok Development and Management Corp. Business Card

A logo design project has been started for our Calgary-Alberta, Canada based land development and project management company. Using this logo, a clean, sleek, professional business card is to be developed (for digital or print media) representing the principals of the company (community, sustainability, and harmony).
Updates

Project Deadline Extended
Reason: Logo design recently completed.

Adobe Illustrator Vector file uploaded. Thanks, Lew

Target Market(s)

Similar business development professionals and other engineering project management personnel involved in land developemtn. Also used to as as the brand and image with both private individuals (Landowners), public officials (policy makers), and investors (banks, venture capitalists).

Industry/Entity Type

Digital

Requirements
Must have
• Open to designers opinion. Based on logo. Must have logo, and space for employee name, title, address, website, office / cell numbers.
Should not have
• No Palm trees or tropical references. Company is based in Calgary, Alberta, Canada.

```html
<!DOCTYPE html>
<html lang="en">
<head>
<meta charset="utf-8">
<title>Varnok Development and Management Corp. Business Card</title>
<link rel="stylesheet" href="https://fonts.googleapis.com/css2?family=Open+Sans:wght@400;600&display=swap">
<style>
  :root {
    --stage: #e6e7e9;
    --charcoal: #2c3038;
    --lime: #9cc12b;
    --grey-text: #8a8e94;
    --ink: #2a2a2a;
    --paper: #ffffff;
    --rule-grey: #9a9a9a;
    --wash: #f1f4e8;
  }
  * { box-sizing: border-box; margin: 0; padding: 0; }
  html, body { width: 1200px; height: 676px; overflow: hidden; background: var(--stage); }
  body { font-family: "Open Sans", Arial, sans-serif; position: relative; }

  .card {
    position: absolute; top: 190px; width: 520px; height: 297px;
    box-shadow: 0 6px 18px rgba(0,0,0,.18); overflow: hidden;
  }
  .card-front { left: 60px; background: var(--charcoal); }
  .card-back { left: 620px; background: var(--paper); }

  /* front */
  .front-brand { position: absolute; left: 60px; top: 70px; }
  .front-brand .mark-square {
    display: inline-block; width: 22px; height: 22px; background: var(--lime);
    margin-right: 14px; vertical-align: middle;
  }
  .front-brand .brand-name {
    font-weight: 600; font-size: 48px; letter-spacing: 4px; color: var(--lime);
    vertical-align: middle;
  }
  .front-tagline {
    position: absolute; left: 96px; top: 136px; font-size: 13px; color: var(--grey-text);
  }
  .front-rule { position: absolute; left: 0; top: 166px; width: 340px; height: 2px; background: var(--lime); }
  .front-website {
    position: absolute; left: 60px; top: 186px; font-size: 19px; letter-spacing: 1px; color: var(--grey-text);
  }
  .front-band { position: absolute; left: 0; bottom: 0; width: 100%; height: 22px; background: var(--lime); }

  /* back */
  .back-brand { position: absolute; left: 40px; top: 34px; }
  .back-brand .mark-square {
    display: inline-block; width: 14px; height: 14px; background: var(--lime);
    margin-right: 10px; vertical-align: middle;
  }
  .back-brand .brand-name {
    font-weight: 600; font-size: 32px; letter-spacing: 3px; color: var(--lime); vertical-align: middle;
  }
  .back-tagline { position: absolute; left: 40px; top: 80px; font-size: 10.5px; color: var(--grey-text); }

  .contact-list { position: absolute; left: 40px; top: 112px; list-style: none; }
  .contact-list li { display: flex; align-items: center; font-size: 14px; color: var(--ink); line-height: 21px; }
  .contact-list svg { width: 10px; height: 10px; margin-right: 10px; fill: var(--lime); }

  .divider { position: absolute; top: 104px; height: 4px; }
  .divider-lime { left: 40px; width: 250px; background: var(--lime); }
  .divider-grey { left: 290px; width: 100px; background: var(--rule-grey); }

  .person { position: absolute; right: 36px; top: 140px; text-align: right; }
  .person-name { font-size: 20px; color: var(--lime); line-height: 22px; }
  .person-title { font-size: 13px; color: var(--ink); }
  .address { position: absolute; right: 56px; top: 196px; text-align: right; font-size: 13px; color: var(--ink); line-height: 17px; }
  .address-pin { position: absolute; right: 36px; top: 214px; width: 12px; height: 16px; fill: var(--ink); }
  .address-rule { position: absolute; right: 36px; top: 190px; width: 90px; height: 3px; background: var(--ink); }

  .back-wash { position: absolute; left: 0; bottom: 0; width: 100%; height: 40px; background: var(--wash); }
</style>
</head>
<body>
  <section class="card card-front">
    <div class="front-brand"><span class="mark-square"></span><span class="brand-name">VARNOK</span></div>
    <p class="front-tagline">Development and Management Corp.</p>
    <div class="front-rule"></div>
    <p class="front-website">www.yourwebsite.com</p>
    <div class="front-band"></div>
  </section>

  <section class="card card-back">
    <div class="back-brand"><span class="mark-square"></span><span class="brand-name">VARNOK</span></div>
    <p class="back-tagline">Development and Management Corp.</p>
    <div class="divider divider-lime"></div>
    <div class="divider divider-grey"></div>

    <ul class="contact-list">
      <li><svg viewBox="0 0 10 10"><path d="M2 0h2l1 3-1.5 1a6 6 0 0 0 2.5 2.5L7 5l3 1v2a2 2 0 0 1-2 2A8 8 0 0 1 0 2a2 2 0 0 1 2-2z"/></svg>0123 456 789</li>
      <li><svg viewBox="0 0 10 10"><rect x="2" y="0" width="6" height="10" rx="1"/></svg>0123 456 789</li>
      <li><svg viewBox="0 0 10 10"><path d="M0 2h10v6H0z"/></svg>youremail@mail.com</li>
      <li><svg viewBox="0 0 10 10"><circle cx="5" cy="5" r="5"/></svg>www.yourwebsite.com</li>
    </ul>

    <div class="person">
      <p class="person-name">your name</p>
      <p class="person-title">designation</p>
    </div>
    <div class="address-rule"></div>
    <p class="address">address (street address<br>suite number, city, state, zip</p>
    <svg class="address-pin" viewBox="0 0 12 16"><path d="M6 0a6 6 0 0 1 6 6c0 4-6 10-6 10S0 10 0 6a6 6 0 0 1 6-6zm0 3.5a2.5 2.5 0 1 0 0 5 2.5 2.5 0 0 0 0-5z"/></svg>

    <div class="back-wash"></div>
  </section>
</body>
</html>
```